Home Page

We provide a Customer Relationship Management (CRM) and Email Marketing solution to medium and small sized businesses with sales teams from 10 to 500 sales people.

Our solution is cloud based and fully supported.

Our solution is unique in that:

1) Email marketing and CRM are in the same system - no transferring data back and forth - sales benefits directly and instantaneously from email analytics and marketing can segment and target messages based on sales intelligence and status.

2) Through our partnership with QuillHarbor.com, each user of our solution gets 500 business contacts they select with email addresses, every month!

3) Our solution is easy to tailor to each unique business and our team gets involved with every new client to help them customize our solution around their unique way of doing business.

So, our solution helps businesses reach more potential customers, close them and keep them.

With 500 potential customers you select each month, our solution lets you nurture them as they move through the sales process via email and afterward, as well as track and manage sales activity, history and pipeline.

Target Market(s)

CEOs, VP of Sales, Marketing Managers

Industry/Entity Type

Marketing

Requirements
Must have
• Trust symbols - KNV
Customer logos - Pell Networks, KNV, Trust of Lanmoor
Feature customer video - http://www.vidplexa.example/watch?feature=player_embedded&v=TRUqzzHwlpX
Graphical representation of our unique proposition - CRM + Email + Leads + Help to Get it working for you
Strong call to action - Start a 30 day free trial

```html
<!DOCTYPE html>
<html lang="en">
<head>
<meta charset="utf-8">
<title>DealCircuit – Online CRM &amp; Email Marketing</title>
<link href="https://fonts.googleapis.com/css2?family=Open+Sans:wght@400;600;700;800&display=swap" rel="stylesheet">
<style>
:root{
  --orange:#f26522;
  --red:#e8452c;
  --nav:#3b3b3b;
  --nav-dark:#2a2a2a;
  --text:#555;
  --heading:#333;
  --light:#f1f1f1;
  --line:#dcdcdc;
  --footer:#2d2d2d;
  --partner:#444;
  --badge:#d4d4d4;
}
*{box-sizing:border-box;margin:0;padding:0}
html,body{width:781px;height:1200px;overflow:hidden}
body{font-family:"Open Sans",Arial,sans-serif;color:var(--text);background:#fff;font-size:8px;line-height:1.45}
.wrap{width:700px;margin:0 auto;position:relative}

.site-header{height:58px}
.site-header .wrap{display:flex;justify-content:space-between;align-items:center;height:58px}
.brand-name{font-size:24px;font-weight:800;color:var(--red);line-height:1}
.brand-tag{font-size:7px;font-weight:700;color:#666;letter-spacing:.5px;margin-top:3px}
.phone{display:flex;align-items:center;gap:6px;font-size:17px;font-weight:600;color:#444}

.main-nav{background:linear-gradient(var(--nav),var(--nav-dark));height:26px}
.main-nav ul{list-style:none;display:flex;justify-content:space-between;height:26px;align-items:center}
.main-nav a{color:#eee;text-decoration:none;font-size:8px;font-weight:600;padding:0 8px}
.main-nav li.active{background:var(--orange);height:26px;display:flex;align-items:center}

.hero{height:290px;background:linear-gradient(#fafafa,#e9e9e9);border-bottom:1px solid var(--line);position:relative}
.hero .wrap{height:290px;display:flex;align-items:center}
.hero-art{width:330px;height:250px;border-radius:6px;background:linear-gradient(135deg,#f7c9a8,#f39a5f 60%,#e0e0e0)}
.hero-copy{flex:1;margin-left:20px;text-align:center}
.hero-copy .formula{font-size:20px;color:var(--orange);font-weight:600;white-space:nowrap}
.hero-copy .promise{font-size:24px;color:var(--orange);font-weight:800;line-height:1.1;margin-top:4px;white-space:nowrap}
.cta{display:inline-block;margin-top:16px;background:var(--orange);color:#fff;font-weight:700;font-size:11px;padding:9px 22px;border-radius:16px;text-decoration:none}
.dots{position:absolute;bottom:8px;left:50%;transform:translateX(-50%);display:flex;gap:4px}
.dots span{width:6px;height:6px;border-radius:50%;background:#bbb}
.dots span.on{background:var(--orange)}

.welcome{padding:18px 0 0;height:200px}
.welcome .wrap{display:flex;gap:20px}
.welcome-text{flex:1}
.welcome-text h2{font-size:12px;color:var(--heading);margin-bottom:8px;font-weight:700}
.welcome-text p{margin-bottom:8px}
.video{width:320px;height:170px;background:linear-gradient(160deg,#7d8a94,#3e4650);border:1px solid #222;position:relative}
.video .bar{position:absolute;left:0;right:0;bottom:0;height:14px;background:#111}
.video svg{position:absolute;left:50%;top:50%;transform:translate(-50%,-50%)}

.start{text-align:center;padding-top:20px;height:78px;border-top:1px solid var(--line);width:700px;margin:0 auto}
.start h2{color:var(--red);font-size:20px;font-weight:600}
.start p{font-size:13px;color:#444;font-weight:600}

.features{height:142px}
.features .wrap{display:flex;gap:24px}
.feature{flex:1}
.feature h3{display:flex;align-items:center;gap:6px;font-size:8px;color:var(--orange);font-weight:700;margin-bottom:6px}
.feature p{margin-bottom:8px}
.more{display:inline-block;background:var(--orange);color:#fff;font-size:7px;font-weight:700;padding:3px 8px;border-radius:3px}

.services{background:var(--light);height:225px;padding-top:14px;border-top:1px solid var(--line)}
.services h2{text-align:center;color:var(--red);font-size:15px;font-weight:600}
.services .sub{text-align:center;font-size:10px;font-weight:700;color:#333;margin-top:4px}
.service-list{display:flex;justify-content:space-between;width:560px;margin:18px auto 0;list-style:none}
.service-list li{text-align:center;font-size:7px;color:#444;font-weight:600;width:70px}
.service-list .ico{width:28px;height:28px;margin:0 auto 4px;display:flex;align-items:center;justify-content:center}
.service-note{width:700px;margin:18px auto 0;background:var(--orange);color:#fff;padding:9px 14px;font-size:7.5px}

.partners{height:110px}
.partners .wrap{display:flex;justify-content:space-around;align-items:center;height:110px}
.partner{font-size:22px;font-weight:700;color:var(--partner)}
.badge{width:120px;height:44px;background:var(--badge);border-radius:2px}

.site-footer{background:var(--footer);height:71px;color:#aaa}
.site-footer .wrap{height:71px;display:flex;flex-direction:column;justify-content:center;align-items:center;gap:6px}
.footer-links{display:flex;gap:12px;font-size:7px;color:#ddd}
.social{position:absolute;right:0;top:10px;display:flex;gap:4px}
.social span{width:14px;height:14px;background:#555;border-radius:2px}
.copyright{font-size:7px}
</style>
</head>
<body>
<header class="site-header">
  <div class="wrap">
    <div class="brand"><div class="brand-name">DealCircuit</div><div class="brand-tag">ONLINE CRM AND EMAIL MARKETING</div></div>
    <div class="phone">
      <svg width="16" height="16" viewBox="0 0 24 24"><path fill="#555" d="M6.6 10.8a15 15 0 0 0 6.6 6.6l2.2-2.2c.3-.3.7-.4 1-.2 1.1.4 2.3.6 3.6.6.6 0 1 .4 1 1V20c0 .6-.4 1-1 1A17 17 0 0 1 3 4c0-.6.4-1 1-1h3.5c.6 0 1 .4 1 1 0 1.3.2 2.5.6 3.6.1.3 0 .7-.2 1z"/></svg>
      (888) 555-0147
    </div>
  </div>
</header>

<nav class="main-nav">
  <ul class="wrap">
    <li class="active"><a href="#">Home</a></li><li><a href="#">CRM Email Marketing</a></li><li><a href="#">Lead Generation</a></li><li><a href="#">Testimonials</a></li><li><a href="#">FAQ</a></li><li><a href="#">Resources</a></li><li><a href="#">Support</a></li><li><a href="#">About Us</a></li><li><a href="#">Contact</a></li><li><a href="#">Blog</a></li>
  </ul>
</nav>

<section class="hero">
  <div class="wrap">
    <div class="hero-art" role="img" aria-label="Illustration of a sales professional working with CRM and email tools"></div>
    <div class="hero-copy">
      <div class="formula">CRM + Email + Leads + Help to</div>
      <div class="promise">GET IT WORKING FOR YOU</div>
      <a class="cta" href="#">START A 30 DAY FREE TRIAL</a>
    </div>
  </div>
  <div class="dots"><span class="on"></span><span></span><span></span><span></span></div>
</section>

<section class="welcome">
  <div class="wrap">
    <div class="welcome-text">
      <h2>Welcome to Online CRM &amp; E-Mail Marketing</h2>
      <p>Our cloud platform joins your contact records, sales pipeline and email campaigns in one place, so every rep sees what prospects open and click the moment it happens. No exports, no duplicate lists, and no waiting on marketing for updates.</p>
      <p>Each user also receives 500 fresh business contacts every month, chosen by you, with verified email addresses ready for your next campaign. Our team helps you tailor the system to the way your business already sells.</p>
    </div>
    <div class="video" role="img" aria-label="Customer testimonial video from vidplexa.example">
      <svg width="34" height="34" viewBox="0 0 34 34"><circle cx="17" cy="17" r="16" fill="rgba(0,0,0,.45)" stroke="#fff" stroke-width="1.5"/><path d="M13 10l11 7-11 7z" fill="#fff"/></svg>
      <div class="bar"></div>
    </div>
  </div>
</section>

<section class="start">
  <h2>Start Online CRM &amp; Email Marketing Today</h2>
  <p>Online CRM Software Salespeople Will Actually Use</p>
</section>

<section class="features">
  <div class="wrap">
    <article class="feature">
      <h3><svg width="14" height="14" viewBox="0 0 14 14"><circle cx="7" cy="7" r="7" fill="#f26522"/><path d="M4 7l2 2 4-4" stroke="#fff" stroke-width="1.6" fill="none"/></svg>Web Based Sales CRM Software</h3>
      <p>Track every contact, deal and task from any browser. Share notes across the team, see full history at a glance and move opportunities through your pipeline with ease.</p>
      <span class="more">Read More</span>
    </article>
    <article class="feature">
      <h3><svg width="14" height="14" viewBox="0 0 14 14"><circle cx="7" cy="7" r="7" fill="#f26522"/><rect x="3.5" y="4.5" width="7" height="5" fill="none" stroke="#fff"/><path d="M3.5 4.5l3.5 3 3.5-3" stroke="#fff" fill="none"/></svg>Unlimited Email Marketing With CRM</h3>
      <p>Send newsletters and drip campaigns straight from your contact lists. Opens and clicks land on each record so reps know exactly who to call next.</p>
      <span class="more">Read More</span>
    </article>
    <article class="feature">
      <h3><svg width="14" height="14" viewBox="0 0 14 14"><circle cx="7" cy="7" r="7" fill="#f26522"/><circle cx="7" cy="5.5" r="2" fill="#fff"/><path d="M3.5 11a3.5 3 0 0 1 7 0z" fill="#fff"/></svg>500 New Leads Every Month</h3>
      <p>Pick 500 new business contacts every month by industry, title and region. They arrive with email addresses, ready to nurture from first touch to closed deal.</p>
      <span class="more">Read More</span>
    </article>
  </div>
</section>

<section class="services">
  <h2>Our Services</h2>
  <p class="sub">Learn More About DealCircuit Online CRM and Email Marketing:</p>
  <ul class="service-list">
    <li><div class="ico"><svg width="24" height="24" viewBox="0 0 24 24"><circle cx="12" cy="12" r="11" fill="#f26522"/><circle cx="12" cy="10" r="3.5" fill="#fff"/><path d="M6 19a6 5 0 0 1 12 0z" fill="#fff"/></svg></div>CRM</li>
    <li><div class="ico"><svg width="24" height="24" viewBox="0 0 24 24"><circle cx="12" cy="12" r="8" fill="none" stroke="#444" stroke-width="2.5"/><circle cx="12" cy="12" r="3" fill="#444"/></svg></div>Automation</li>
    <li><div class="ico"><svg width="24" height="24" viewBox="0 0 24 24"><rect x="3" y="6" width="18" height="12" fill="none" stroke="#444" stroke-width="2"/><path d="M3 6l9 7 9-7" stroke="#444" stroke-width="2" fill="none"/></svg></div>E-mail</li>
    <li><div class="ico"><svg width="24" height="24" viewBox="0 0 24 24"><circle cx="8" cy="9" r="3" fill="#444"/><circle cx="16" cy="9" r="3" fill="#444"/><path d="M2 19a6 5 0 0 1 12 0zM10 19a6 5 0 0 1 12 0z" fill="#444"/></svg></div>Collaboration</li>
    <li><div class="ico"><svg width="24" height="24" viewBox="0 0 24 24"><path d="M4 20l10-10M14 4l6 6-4 4-6-6z" stroke="#444" stroke-width="2.5" fill="none"/></svg></div>Customizable</li>
    <li><div class="ico"><svg width="24" height="24" viewBox="0 0 24 24"><rect x="4" y="12" width="4" height="8" fill="#444"/><rect x="10" y="7" width="4" height="13" fill="#444"/><rect x="16" y="4" width="4" height="16" fill="#444"/></svg></div>Analytics</li>
    <li><div class="ico"><svg width="24" height="24" viewBox="0 0 24 24"><path d="M4 13a8 8 0 0 1 16 0" stroke="#444" stroke-width="2.5" fill="none"/><rect x="3" y="12" width="4" height="7" rx="1" fill="#444"/><rect x="17" y="12" width="4" height="7" rx="1" fill="#444"/></svg></div>Support</li>
  </ul>
  <p class="service-note">DealCircuit is an online CRM and email marketing system that helps small and mid-sized sales teams reach more prospects, close them faster and keep them longer. Get started today with a free trial and our team will set it up around the way you work.</p>
</section>

<section class="partners">
  <div class="wrap">
    <span class="partner">Pell Networks</span>
    <div class="badge" role="img" aria-label="KNV accreditation badge"></div>
    <span class="partner">Trust of Lanmoor</span>
  </div>
</section>

<footer class="site-footer">
  <div class="wrap">
    <div class="footer-links"><span>Home</span><span>Resources</span><span>CRM</span><span>Email</span><span>Sales</span><span>Support</span><span>Privacy Policy</span><span>Affiliates</span><span>Members</span><span>Sitemap</span></div>
    <div class="copyright">© 2024 DealCircuit. All rights reserved.</div>
    <div class="social"><span></span><span></span><span></span><span></span></div>
  </div>
</footer>
</body>
</html>
```